KL Taxidermy

I need business Cards with my logo and a background photo of one of my taxidermy mounts.
I would like a black back drop behind it all and what ever looks best for my contact information (red or white?)
Garrick Pembley
592-718-4409
kltaxidermy482@mailnook.example
Chatterloom page

```html
<!DOCTYPE html>
<html lang="en">
<head>
<meta charset="utf-8">
<title>KL Taxidermy – Business Card</title>
<link rel="stylesheet" href="https://fonts.googleapis.com/css2?family=Open+Sans:wght@400;700&display=swap">
<style>
  :root {
    --backdrop: #2e2e30;
    --card-black: #0d0d0d;
    --card-back: #1a1a1b;
    --card-back-mark: #262628;
    --card-white: #ffffff;
    --accent-red: #e3262b;
    --ink-white: #ffffff;
    --ink-black: #0d0d0d;
  }
  * { margin: 0; padding: 0; box-sizing: border-box; }
  html, body {
    width: 1200px; height: 900px; overflow: hidden;
    background: var(--backdrop);
    font-family: "Open Sans", Arial, sans-serif;
  }
  .canvas { position: relative; width: 1200px; height: 900px; }

  .card {
    position: absolute; left: 290px;
    width: 620px; height: 354px;
    overflow: hidden;
  }

  /* Back side */
  .card--back { top: 60px; background: var(--card-back); }
  .card--back .back-mark {
    position: absolute; left: 0; right: 0; top: 150px;
    text-align: center;
    font-size: 40px; font-weight: 700; letter-spacing: 3px;
    text-transform: uppercase;
    color: var(--card-back-mark);
  }

  /* Front side */
  .card--front { top: 486px; background: var(--card-white); }
  .front-shapes { position: absolute; inset: 0; }
  .brand-name {
    position: absolute; left: 0; right: 0; top: 88px;
    text-align: center;
    font-size: 34px; font-weight: 700; letter-spacing: 3px;
    text-transform: uppercase;
    color: var(--ink-black);
  }
  .holder-name {
    position: absolute; left: 40px; top: 262px;
    font-size: 22px; font-weight: 700;
    text-transform: uppercase;
    color: var(--ink-white);
  }
  .divider {
    position: absolute; left: 292px; top: 248px;
    width: 2px; height: 72px; background: var(--ink-white);
  }
  .contact-list {
    position: absolute; left: 312px; top: 254px;
    list-style: none;
    color: var(--ink-white); font-size: 15px;
  }
  .contact-list li { display: flex; align-items: center; gap: 10px; margin-bottom: 10px; }
  .contact-list svg { width: 16px; height: 16px; fill: var(--ink-white); flex: none; }
  .social-name {
    position: absolute; right: 30px; top: 246px;
    font-size: 14px; font-weight: 400;
    color: var(--ink-white);
  }
</style>
</head>
<body>
<main class="canvas">

  <section class="card card--back" aria-label="Card back">
    <div class="back-mark">KL Taxidermy</div>
  </section>

  <section class="card card--front" aria-label="Card front">
    <svg class="front-shapes" viewBox="0 0 620 354" width="620" height="354" aria-hidden="true">
      <polygon points="0,198 290,198 330,244 460,218 620,218 620,354 0,354" fill="var(--card-black)"/>
      <polygon points="300,210 330,244 400,230" fill="var(--accent-red)"/>
    </svg>

    <div class="brand-name">KL Taxidermy</div>

    <div class="holder-name">Garrick Pembley</div>
    <div class="divider"></div>
    <ul class="contact-list">
      <li>
        <svg viewBox="0 0 24 24"><path d="M6.6 10.8a15.1 15.1 0 0 0 6.6 6.6l2.2-2.2a1 1 0 0 1 1-.25 11.4 11.4 0 0 0 3.6.57 1 1 0 0 1 1 1V20a1 1 0 0 1-1 1A17 17 0 0 1 3 4a1 1 0 0 1 1-1h3.5a1 1 0 0 1 1 1c0 1.25.2 2.45.57 3.57a1 1 0 0 1-.25 1z"/></svg>
        <span>592-718-4409</span>
      </li>
      <li>
        <svg viewBox="0 0 24 24"><path d="M2 5h20v14H2z M4 7v.5l8 5 8-5V7l-8 5z" fill-rule="evenodd"/></svg>
        <span>kltaxidermy482@mailnook.example</span>
      </li>
    </ul>
    <div class="social-name">Chatterloom</div>
  </section>

</main>
</body>
</html>
```